Redline Vortex Racing

we would like to create a new sponsorship proposal brochure that can be amended to suit each new proposal sent.
Attached is the following:
1. Redline Vortex racing logo (please use the bottom one)
2. Photo of our current car racing that can be used
3. Proposed race car artwork for new proposal to Corvane Lubes (you can use any of the images shown preferably the side elevation)
The proposal will have the following pages included:
1.Front page
2. Introduction & Bio of the race team
3. 3 Year Plan
4. Race Series (Varnaclass, Falko Trophy Series (Brindell Championships)
5. Sponsorship benefits
6. Cost of Racing
7. Contacts Page
The brochure is to be professional however we would like it to be cool and fun. Happy to provide feedback on options provided. the content for each page will be filled by us please allow the text areas within your designs.
Target Market(s)
Corporate Business looking to get their brand out.
Industry/Entity Type
Car Racing

```html
<!DOCTYPE html>
<html lang="en">
<head>
<meta charset="utf-8">
<title>Redline Vortex Racing – Sponsorship Brochure Cover</title>
<link rel="stylesheet" href="https://fonts.googleapis.com/css2?family=Roboto:ital,wght@0,400;0,500;0,700;1,900&family=Questrial&family=Playball&display=swap">
<style>
  :root {
    --race-red: #e0121b;
    --deep-red: #b50d14;
    --panel-top: #3b3c40;
    --panel-bottom: #1c1d20;
    --text-light: #f2f2f2;
    --text-body: #d8d8d8;
    --stage: #dcdcdc;
    --white: #ffffff;
  }
  * { box-sizing: border-box; margin: 0; padding: 0; }
  html, body {
    width: 1200px; height: 849px; overflow: hidden;
    background: var(--stage);
  }
  .brochure-wrap {
    position: absolute; left: 20px; top: 48px;
    width: 1160px; height: 752px;
  }
  .brochure {
    position: absolute; left: 0; top: 0;
    width: 1063px; height: 689px;
    transform: scale(1.0913); transform-origin: 0 0;
    overflow: hidden;
    font-family: "Questrial", sans-serif;
    color: var(--text-light);
  }
  .brochure-art { position: absolute; inset: 0; width: 1063px; height: 689px; }

  /* Back panel */
  .section-title {
    position: absolute; left: 28px;
    font-family: "Roboto", sans-serif; font-weight: 900; font-style: italic;
    font-size: 19px; color: var(--race-red);
  }
  .section-title--about { top: 294px; }
  .section-title--contact { top: 530px; }
  .title-rule {
    position: absolute; left: 28px; height: 1px; background: var(--race-red);
  }
  .title-rule::after {
    content: ""; position: absolute; right: -6px; top: -3px;
    width: 6px; height: 6px; border: 1px solid var(--race-red); border-radius: 50%;
  }
  .title-rule--about { top: 323px; width: 300px; }
  .title-rule--contact { top: 557px; width: 182px; }
  .about-copy {
    position: absolute; left: 28px; top: 340px; width: 482px;
    font-family: "Roboto", sans-serif; font-size: 9.6px; line-height: 12.7px;
    color: var(--text-body);
  }
  .about-copy p + p { margin-top: 12px; }

  .contact-list {
    position: absolute; left: 28px; top: 578px; width: 420px;
    display: grid; grid-template-columns: 180px 220px; row-gap: 14px;
    list-style: none;
  }
  .contact-item {
    display: flex; align-items: center; gap: 10px;
    font-size: 15px; color: var(--text-light);
  }
  .contact-item svg { width: 16px; height: 16px; flex: none; }

  /* Front panel */
  .team-name {
    position: absolute; left: 600px; top: 360px; width: 400px;
    text-align: center; font-family: "Roboto", sans-serif; font-weight: 700;
    font-size: 38px; line-height: 40px; text-transform: uppercase;
    color: var(--white); letter-spacing: 1px;
  }
  .tagline {
    position: absolute; left: 600px; width: 400px; text-align: center;
    color: var(--white);
  }
  .tagline--lead {
    top: 508px; font-family: "Roboto", sans-serif; font-size: 23px;
  }
  .tagline--script {
    top: 538px; font-family: "Playball", cursive; font-size: 38px;
  }
  .front-quote {
    position: absolute; left: 555px; top: 596px; width: 490px;
    text-align: center; font-family: "Roboto", sans-serif; font-weight: 500;
    font-size: 12.5px; line-height: 18px; color: var(--white);
  }
  .front-quote b { font-size: 17px; font-weight: 700; }
  .front-phone {
    position: absolute; left: 537px; top: 636px;
    display: flex; align-items: center; gap: 6px;
    font-family: "Roboto", sans-serif; font-size: 22px; color: var(--white);
  }
  .front-phone svg { width: 24px; height: 24px; }
  .front-web {
    position: absolute; right: 35px; top: 641px;
    font-family: "Roboto", sans-serif; font-size: 16.5px; color: var(--white);
  }
</style>
</head>
<body>
<div class="brochure-wrap">
  <div class="brochure">
    <svg class="brochure-art" viewBox="0 0 1063 689" xmlns="http://www.w3.org/2000/svg">
      <defs>
        <linearGradient id="panelShade" x1="0" y1="0" x2="0" y2="1">
          <stop offset="0" stop-color="#3b3c40"/>
          <stop offset="1" stop-color="#1c1d20"/>
        </linearGradient>
        <linearGradient id="backPhotoTone" x1="0" y1="0" x2="0" y2="1">
          <stop offset="0" stop-color="#c9c4bd"/>
          <stop offset="0.35" stop-color="#8a8c86"/>
          <stop offset="0.55" stop-color="#7b9a4e"/>
          <stop offset="0.8" stop-color="#a99176"/>
          <stop offset="1" stop-color="#b98a6d"/>
        </linearGradient>
        <linearGradient id="frontPhotoTone" x1="0" y1="0" x2="0" y2="1">
          <stop offset="0" stop-color="#8f5a3c"/>
          <stop offset="0.3" stop-color="#7a6b43"/>
          <stop offset="0.45" stop-color="#9aa0a3"/>
          <stop offset="0.7" stop-color="#c43a34"/>
          <stop offset="1" stop-color="#6f7174"/>
        </linearGradient>
      </defs>

      <rect class="panel-base" width="1063" height="689" fill="url(#panelShade)"/>

      <g role="img" aria-label="Photo of the red team race car speeding along the track, motion blurred">
        <polygon points="0,0 531,0 531,300 0,115" fill="url(#backPhotoTone)"/>
      </g>
      <g role="img" aria-label="Photo of the red team race car leading a white car around a corner">
        <polygon points="531,0 1063,0 1063,182 918,365 531,362" fill="url(#frontPhotoTone)"/>
      </g>

      <polygon class="accent-stripe" points="40,128 531,292 705,362 690,366 531,318 60,140" fill="#e0121b"/>
      <polygon class="accent-stripe" points="531,300 705,362 531,362" fill="#b50d14"/>
      <polygon class="accent-stripe" points="1063,212 1063,238 935,372 905,372" fill="#e0121b"/>

      <rect class="edge-band" x="1043" y="402" width="20" height="287" fill="#e0121b"/>
      <rect class="base-band" x="0" y="672" width="276" height="17" fill="#e0121b"/>
      <rect class="base-band" x="276" y="672" width="608" height="17" fill="#ffffff"/>
      <rect class="base-band" x="884" y="672" width="179" height="17" fill="#e0121b"/>
    </svg>

    <!-- Back panel -->
    <h2 class="section-title section-title--about">What is Lorem Ipsum?</h2>
    <div class="title-rule title-rule--about"></div>
    <div class="about-copy">
      <p>Lorem Ipsum is simply dummy text of the printing and typesetting industry. Lorem Ipsum has been the industry's standard dummy text ever since the 1500s, when an unknown printer took a galley of type and scrambled it to make a type specimen book. It has survived not only five centuries, but also the leap into electronic typesetting, remaining essentially unchanged. It was popularised in the 1960s with the release of Letraset sheets containing Lorem Ipsum passages, and more recently with desktop publishing software like Aldus PageMaker including versions of Lorem Ipsum.</p>
      <p>Sed ut perspiciatis unde omnis iste natus error sit voluptatem accusantium doloremque laudantium, totam rem aperiam, eaque ipsa quae ab illo inventore veritatis et quasi architecto beatae vitae dicta sunt explicabo. Nemo enim ipsam voluptatem quia voluptas sit aspernatur aut odit aut fugit, sed quia consequuntur magni dolores eos qui ratione voluptatem sequi nesciunt. Neque porro quisquam est, qui dolorem ipsum quia dolor sit amet, consectetur, adipisci velit, sed quia non numquam eius modi tempora incidunt ut labore et dolore magnam aliquam quaerat voluptatem.</p>
    </div>

    <h2 class="section-title section-title--contact">Contact US</h2>
    <div class="title-rule title-rule--contact"></div>
    <ul class="contact-list">
      <li class="contact-item">
        <svg viewBox="0 0 16 16"><path d="M8 1a5 5 0 0 0-5 5c0 3.6 5 9 5 9s5-5.4 5-9a5 5 0 0 0-5-5zm0 7a2 2 0 1 1 0-4 2 2 0 0 1 0 4z" fill="#e0121b"/></svg>
        Address Is Here
      </li>
      <li class="contact-item">
        <svg viewBox="0 0 16 16"><rect x="1" y="3" width="14" height="10" rx="1" fill="#e0121b"/><path d="M1.5 4 8 9l6.5-5" stroke="#2a2b2e" stroke-width="1.2" fill="none"/></svg>
        Mail Id Is Here
      </li>
      <li class="contact-item">
        <svg viewBox="0 0 16 16"><g fill="none" stroke="#e0121b" stroke-width="1.2"><circle cx="8" cy="8" r="6.2"/><ellipse cx="8" cy="8" rx="2.8" ry="6.2"/><path d="M2 8h12M3 5h10M3 11h10"/></g></svg>
        Website Is Here
      </li>
      <li class="contact-item">
        <svg viewBox="0 0 16 16"><circle cx="8" cy="8" r="7" fill="none" stroke="#e0121b" stroke-width="1.2"/><path d="M5.2 4.3l1.5-.3.8 2-1 .8c.5 1.2 1.3 2 2.5 2.5l.8-1 2 .8-.3 1.5c-3.4.3-6.6-2.9-6.3-6.3z" fill="#e0121b"/></svg>
        Phone Number Is Here
      </li>
    </ul>

    <!-- Front panel -->
    <h1 class="team-name">Redline Vortex<br>Racing</h1>
    <p class="tagline tagline--lead">A Smooth Running is</p>
    <p class="tagline tagline--script">Relaxing Experience</p>
    <p class="front-quote"><b>“</b> There is no one who loves pain itself, who seeks after it and wants to have it,<br>simply because it is pain...<b>”</b></p>
    <div class="front-phone">
      <svg viewBox="0 0 24 24"><circle cx="12" cy="12" r="10.5" fill="none" stroke="#e0121b" stroke-width="1.5"/><path d="M8 6.3l2.2-.5 1.2 3-1.5 1.2c.8 1.8 2 3 3.8 3.8l1.2-1.5 3 1.2-.5 2.2C12.3 16.2 7.8 11.7 8 6.3z" fill="#e0121b"/></svg>
      123-456-7890
    </div>
    <div class="front-web">www.websiteaddress.com</div>
  </div>
</div>
</body>
</html>
```